"Recently Leased" flyer for real estate agency

Looking to have a Recently Leased flyer designed. This will be delivered to apartments and houses closely situated to a property we have recently leased. The idea is to get the attention of owner/landlords in the area that may be considering leasing their property in the future and inform them of the great work we are doing locally. I would like the design to be a two sided flyer using the photoshop (PSD) template below (we would like to be able to edit this once complete should we need to update copy etc in the future). I would like the front page to look like our "for lease sign with the leased sticker on it and copy, I dont want it to look like a typical junk mail flyer.

Target Market(s)

Property owners and investors, male and female aged 28-70

Industry/Entity Type

Real Estate

Font styles to use
Sans Serif

Colors

Designer to choose colors to be used in the design.

Requirements
Must have
• Harbor Keystone Logo
• Contact information
• Copy supplied
Nice to have
• Slick, clean design,
Should not have
• too many colours or too busy a design.
• NO PROPERTY PHOTOS ON FRONT - I want this to be generic and not relate to a specific property image which might confuse people.

```html
<!DOCTYPE html>
<html lang="en">
<head>
<meta charset="utf-8">
<title>Harbor Keystone – Recently Leased Flyer</title>
<link href="https://fonts.googleapis.com/css2?family=Montserrat:wght@400;600;700;800&family=Open+Sans:wght@400;600;700&display=swap" rel="stylesheet">
<style>
  :root{
    --charcoal:#2b2b2d;
    --charcoal-dark:#1f1f21;
    --charcoal-light:#3a3a3d;
    --teal:#2fa3b3;
    --teal-dark:#1f7f8c;
    --red:#d9262b;
    --white:#ffffff;
    --ink:#3a3a3c;
    --page:#e9e9ea;
  }
  *{box-sizing:border-box;margin:0;padding:0}
  html,body{width:733px;height:1200px;overflow:hidden;background:var(--page)}
  body{font-family:"Open Sans",Arial,sans-serif;color:var(--ink)}
  .sheet{width:733px;height:1200px;display:flex;justify-content:center;align-items:center;gap:15px}
  .flyer{width:345px;height:730px;background:var(--white);display:flex;flex-direction:column;box-shadow:0 2px 10px rgba(0,0,0,.18);overflow:hidden}
  .flyer-header{background:var(--charcoal);height:96px;flex:none;display:flex;align-items:center;justify-content:center;gap:8px}
  .brand-mark{width:10px;height:10px;background:var(--teal)}
  .brand-name{font-family:"Montserrat",Arial,sans-serif;font-weight:700;font-size:21px;letter-spacing:.5px;color:var(--white)}
  .hero{position:relative;height:210px;flex:none}
  .hero--sign{background:linear-gradient(180deg,var(--charcoal) 0%,var(--charcoal-light) 100%)}
  .sign-stripe{position:absolute;left:0;right:0;bottom:0;height:8px;background:var(--teal)}
  .hero--photo{background:linear-gradient(180deg,#4f95cf 0%,#9cc6e6 35%,#4c7a55 60%,#2b9bc4 85%,#1e7aa8 100%)}
  .leased-banner{position:absolute;left:0;top:8px;background:var(--red);color:var(--white);font-family:"Montserrat",Arial,sans-serif;font-weight:800;font-size:22px;padding:4px 14px 4px 12px;letter-spacing:.5px}
  .flyer-body{flex:1;padding:16px 18px 10px;font-size:9.6px;line-height:1.5}
  .intro{margin-bottom:10px}
  .benefits{list-style:none;margin-bottom:10px}
  .benefits li{display:flex;gap:6px;margin-bottom:6px;align-items:flex-start}
  .benefits svg{flex:none;margin-top:2px}
  .closing{font-weight:700}
  .flyer-footer{background:var(--teal);height:108px;flex:none;display:flex;flex-direction:column}
  .agent-row{flex:1;display:flex;align-items:center;padding:0 12px;gap:10px}
  .agent-photo{width:58px;height:70px;flex:none;background:linear-gradient(180deg,#c9d2d6,#8a9aa2);border:2px solid var(--white)}
  .agent-info{flex:1;min-width:0}
  .agent-name{font-family:"Montserrat",Arial,sans-serif;font-weight:800;font-size:16px;color:var(--white);line-height:1;white-space:nowrap}
  .agent-role{font-size:7px;color:var(--white);letter-spacing:1px;margin-top:4px;font-weight:600;white-space:nowrap}
  .call-box{flex:none;background:var(--white);padding:4px 8px;text-align:center}
  .call-label{font-family:"Montserrat",Arial,sans-serif;font-size:7px;font-weight:700;color:var(--teal-dark);letter-spacing:1px}
  .call-number{font-family:"Montserrat",Arial,sans-serif;font-size:14px;font-weight:800;color:var(--charcoal);white-space:nowrap}
  .contact-strip{background:var(--charcoal-dark);color:var(--white);font-size:7px;padding:4px 12px;display:flex;justify-content:space-between}
</style>
</head>
<body>
<main class="sheet">

  <section class="flyer flyer--front">
    <header class="flyer-header">
      <span class="brand-mark"></span>
      <span class="brand-name">HARBOR KEYSTONE</span>
    </header>
    <div class="hero hero--sign">
      <div class="leased-banner">LEASED!</div>
      <div class="sign-stripe"></div>
    </div>
    <div class="flyer-body">
      <p class="intro">We recently leased a property in your building or street. Attracting a great tenant quickly comes down to pricing, presentation and reaching the right people. Here is why local owners choose us:</p>
      <ul class="benefits">
        <li><svg width="9" height="9" viewBox="0 0 10 10"><path d="M1 5l3 3 5-6" fill="none" stroke="var(--teal)" stroke-width="2"/></svg>We lease our properties two weeks faster than the local average</li>
        <li><svg width="9" height="9" viewBox="0 0 10 10"><path d="M1 5l3 3 5-6" fill="none" stroke="var(--teal)" stroke-width="2"/></svg>A strong database of tenants actively looking in this area</li>
        <li><svg width="9" height="9" viewBox="0 0 10 10"><path d="M1 5l3 3 5-6" fill="none" stroke="var(--teal)" stroke-width="2"/></svg>Leasing is all we do, with no sales and no distractions</li>
        <li><svg width="9" height="9" viewBox="0 0 10 10"><path d="M1 5l3 3 5-6" fill="none" stroke="var(--teal)" stroke-width="2"/></svg>A money back guarantee on our level of service</li>
        <li><svg width="9" height="9" viewBox="0 0 10 10"><path d="M1 5l3 3 5-6" fill="none" stroke="var(--teal)" stroke-width="2"/></svg>Highly competitive, simple all-inclusive pricing</li>
        <li><svg width="9" height="9" viewBox="0 0 10 10"><path d="M1 5l3 3 5-6" fill="none" stroke="var(--teal)" stroke-width="2"/></svg>Experience the difference of a proactive management approach</li>
      </ul>
      <p class="closing">Contact Sam today for a free rental appraisal and find out how much your property could earn.</p>
    </div>
    <footer class="flyer-footer">
      <div class="agent-row">
        <div class="agent-photo" role="img" aria-label="Portrait of the leasing agent"></div>
        <div class="agent-info">
          <div class="agent-name">SAM CARTER</div>
          <div class="agent-role">PROPERTY MANAGER</div>
        </div>
        <div class="call-box">
          <div class="call-label">CALL NOW</div>
          <div class="call-number">0400 123 456</div>
        </div>
      </div>
      <div class="contact-strip"><span>E: sam@harborkeystone.com</span><span>W: harborkeystone.com</span></div>
    </footer>
  </section>

  <section class="flyer flyer--back">
    <header class="flyer-header">
      <span class="brand-mark"></span>
      <span class="brand-name">HARBOR KEYSTONE</span>
    </header>
    <div class="hero hero--photo" role="img" aria-label="Photo of a resort-style pool with palm trees overlooking the sea">
      <div class="leased-banner">LEASED!</div>
    </div>
    <div class="flyer-body">
      <p class="intro">This fantastic home was recently leased by our team in under a week. Our local knowledge and careful tenant selection delivered a great result for the owner.</p>
      <ul class="benefits">
        <li><svg width="9" height="9" viewBox="0 0 10 10"><path d="M1 5l3 3 5-6" fill="none" stroke="var(--teal)" stroke-width="2"/></svg>Thorough tenant checks and reference screening</li>
        <li><svg width="9" height="9" viewBox="0 0 10 10"><path d="M1 5l3 3 5-6" fill="none" stroke="var(--teal)" stroke-width="2"/></svg>Simple, transparent fees with no hidden extras</li>
        <li><svg width="9" height="9" viewBox="0 0 10 10"><path d="M1 5l3 3 5-6" fill="none" stroke="var(--teal)" stroke-width="2"/></svg>Regular inspections and detailed condition reports</li>
        <li><svg width="9" height="9" viewBox="0 0 10 10"><path d="M1 5l3 3 5-6" fill="none" stroke="var(--teal)" stroke-width="2"/></svg>Fast, friendly communication with every owner</li>
        <li><svg width="9" height="9" viewBox="0 0 10 10"><path d="M1 5l3 3 5-6" fill="none" stroke="var(--teal)" stroke-width="2"/></svg>We find quality tenants within thirty days</li>
      </ul>
      <p class="closing">Call Sam for a no obligation chat about leasing your property.</p>
    </div>
    <footer class="flyer-footer">
      <div class="agent-row">
        <div class="agent-photo" role="img" aria-label="Portrait of the leasing agent"></div>
        <div class="agent-info">
          <div class="agent-name">SAM CARTER</div>
          <div class="agent-role">PROPERTY MANAGER</div>
        </div>
        <div class="call-box">
          <div class="call-label">CALL NOW</div>
          <div class="call-number">0400 123 456</div>
        </div>
      </div>
      <div class="contact-strip"><span>E: sam@harborkeystone.com</span><span>W: harborkeystone.com</span></div>
    </footer>
  </section>

</main>
</body>
</html>
```